【 概要 】 ホームページのTOP画像のデザインを募集いたします。 飲食店専用ホームページ制作です。 メインターゲットは飲食店オーナーの方々です。 飲食のホームページにあった「どんなお店なのか」、「どんなメニュ・どんなコースがあるか」など、 そのお店を気になった方々に来店を促すようなTOP画像が希望です。 【 依頼内容 】 ・サイズ:1920px×1080px ・作成数: 1種類 ・利用用途:ホームページトップ画像 ・色:オレンジ/赤/黄色 ・文言:あなたのお店をオリジナルデザインで作ってみませんか? 【 デザインイメージ 】 ・雰囲気:信頼感、安心感があり、ポップ感 ・現在制作途中のホームページにあった感じ http://sampwebnoren.com/ ・参考他社デザイン https://www.hanamuraya.co.jp/menu/kikaku/ また飲食以外も対象にしたいと思ったので別案も制作していただけたら幸いです。 【 依頼内容 】 色:グレー/白/黒 文言:ホームページはオリジナルデザインで! 参考URL:https://qv-webworks.jp/hp/?utm_source=kensaku&utm_medium=cpc&qclid=QRS.2004815367.PXbTwLcdFhZNruqk5p8w27AKRGetSd3hvm-qWFBCZjBXFgKQ5_E_CzX 【 契約金額(税抜) 】 1万円 ※契約金額(税込)からシステム利用料を差し引いた金額が、ワーカーさまの受取金額となります その他ご質問等ありましたら、気軽にお問い合わせください。 ご応募をお待ちしております! |
| https://www.hanamuraya.co.jp/menu/kikaku/ | ||
私共の内容をよく理解していただいた上で作成していただきありがとうございます。
今回korunote様のご提案が弊社のHPの表画面での使用に一番最適だと考え作用させていただきます。
皆様色々ご提案ありがとうございます。とても素敵なデザインを見していただきました。
弊社は今後よくご依頼などをさせていただきますので、その際は皆様また力を貸していただければと思います。

```html
<!DOCTYPE html>
<html lang="ja">
<head>
<meta charset="utf-8">
<title>ホームページはオリジナルデザインで!</title>
<link href="https://fonts.googleapis.com/css2?family=Noto+Sans+JP:wght@700;900&display=swap" rel="stylesheet">
<style>
  :root {
    --bg: #e6e9eb;
    --bg-light: #f1f3f4;
    --stripe: rgba(255,255,255,0.55);
    --stripe-shade: rgba(190,196,200,0.35);
    --ink: #1c1c1c;
    --card: #f4f5f6;
    --icon-navy: #2c3e66;
    --icon-teal: #2b8a8a;
    --scene-a: #d5dadd;
    --scene-b: #b9c3c8;
  }
  * { margin: 0; padding: 0; box-sizing: border-box; }
  html, body { width: 1200px; height: 676px; overflow: hidden; }
  body { font-family: "Noto Sans JP", sans-serif; color: var(--ink); background: var(--bg); }
  .hero { position: relative; width: 1200px; height: 676px; overflow: hidden; background: linear-gradient(120deg, var(--bg-light), var(--bg)); }
  .hero-stripes { position: absolute; inset: 0; }
  .headline { position: absolute; left: 100px; top: 224px; font-weight: 900; }
  .headline-lead { display: block; font-size: 44px; letter-spacing: 0.5px; line-height: 1.1; }
  .headline-main { display: block; margin-top: 24px; font-size: 46px; letter-spacing: 0.5px; line-height: 1; white-space: nowrap; }
  .headline-main .accent { display: inline-block; padding-bottom: 12px; border-bottom: 4px solid var(--ink); }
  .headline-main .tail { font-size: 32px; margin-left: 6px; }
  .features { position: absolute; left: 94px; top: 400px; display: flex; gap: 14px; list-style: none; }
  .feature { width: 152px; height: 156px; background: var(--card); display: flex; flex-direction: column; align-items: center; justify-content: flex-end; padding-bottom: 22px; }
  .feature svg { width: 64px; height: 64px; margin-bottom: 18px; }
  .feature-label { font-size: 18px; font-weight: 700; white-space: nowrap; }
  .scene { position: absolute; left: 636px; top: 176px; width: 544px; height: 488px; border-radius: 8px; background: linear-gradient(160deg, var(--scene-a), var(--scene-b)); }
</style>
</head>
<body>
<main class="hero">
  <svg class="hero-stripes" width="1200" height="676" viewBox="0 0 1200 676" aria-hidden="true">
    <polygon points="0,560 560,0 720,0 160,676 0,676" fill="var(--stripe)"/>
    <polygon points="330,676 1006,0 1200,0 1200,40 564,676" fill="var(--stripe-shade)"/>
    <polygon points="760,676 1200,236 1200,380 904,676" fill="var(--stripe)"/>
    <polygon points="0,240 240,0 300,0 0,300" fill="var(--stripe-shade)"/>
  </svg>

  <h1 class="headline">
    <span class="headline-lead">ホームページは</span>
    <span class="headline-main"><span class="accent">オリジナルデザイン</span><span class="tail">で!</span></span>
  </h1>

  <ul class="features">
    <li class="feature">
      <svg viewBox="0 0 64 64" fill="none" stroke="var(--icon-navy)" stroke-width="3" stroke-linejoin="round" stroke-linecap="round" aria-hidden="true">
        <path d="M2 24 L14 18 L24 36 L12 42 Z"/>
        <path d="M62 24 L50 18 L40 36 L52 42 Z"/>
        <path d="M18 24 L28 20 L36 24 L48 22" stroke="var(--icon-teal)"/>
        <path d="M22 38 L32 46 C34 48 37 46 35 43 M28 40 L36 46 C38 48 41 45 39 43 M34 40 L40 44 C42 45 44 42 42 40 L34 32 L28 34"/>
      </svg>
      <span class="feature-label">安心サポート</span>
    </li>
    <li class="feature">
      <svg viewBox="0 0 64 64" fill="none" stroke="var(--icon-navy)" stroke-width="3" stroke-linejoin="round" stroke-linecap="round" aria-hidden="true">
        <path d="M26 8 L38 8 L34 14 L30 14 Z"/>
        <path d="M30 14 C18 20 18 38 32 38 C46 38 46 20 34 14"/>
        <path d="M28 22 L32 27 L36 22 M32 27 L32 34 M28 28 L36 28 M28 31 L36 31" stroke="var(--icon-teal)" stroke-width="2.5"/>
        <path d="M6 46 L16 42 C22 40 28 44 34 44 L40 44 C43 44 43 48 40 48 L30 48 M40 48 L54 42 C58 40 60 44 57 46 L40 56 L16 56 L6 58"/>
      </svg>
      <span class="feature-label">低価格</span>
    </li>
    <li class="feature">
      <svg viewBox="0 0 64 64" fill="none" stroke="var(--icon-navy)" stroke-width="3" stroke-linecap="round" aria-hidden="true">
        <circle cx="38" cy="26" r="18"/>
        <path d="M25 39 L8 56" stroke-width="5"/>
        <circle cx="38" cy="22" r="5" stroke="var(--icon-teal)" stroke-width="2.5"/>
        <path d="M29 36 C30 30 46 30 47 36" stroke="var(--icon-teal)" stroke-width="2.5"/>
      </svg>
      <span class="feature-label">オーダーメイド</span>
    </li>
  </ul>

  <div class="scene" role="img" aria-label="パソコン・タブレット・スマートフォンに表示されたウェブサイトと、その前に並ぶビジネスパーソンたちのイラスト"></div>
</main>
</body>
</html>
```